Banner for fencing on construction sites

Banner to market our company on construction job sites Included on banner we would need something along the lines "Temp Labor" and our website "WWW.KTRVB.COM" all Visible enough to see as people are driving by.
The attached .ai file we provided has two images, we prefer the 2nd one with just RVB.
The Banner will be 7ft wide x 4ft height.

Target Market(s)

Construction Companies

Requirements
Must have
• Visible Website to drivers passing by
• RVB Logo has to be BIGGER than anything

```html
<!DOCTYPE html>
<html lang="en">
<head>
<meta charset="utf-8">
<title>RVB Temp Labor – Site Fence Banner</title>
<link rel="stylesheet" href="https://fonts.googleapis.com/css2?family=Montserrat:ital,wght@0,800;0,900;1,900&display=swap">
<style>
  :root {
    --page-bg: #e6e6e6;
    --banner-black: #0b0b0b;
    --frame-amber: #f7ac3c;
    --brand-orange: #f39a2e;
    --tagline-red: #ea521d;
    --url-white: #ffffff;
  }
  * { margin: 0; padding: 0; box-sizing: border-box; }
  html, body {
    width: 1200px;
    height: 1000px;
    overflow: hidden;
    background: var(--page-bg);
    font-family: "Montserrat", Arial, sans-serif;
  }
  .banner {
    position: absolute;
    left: 68px;
    top: 198px;
    width: 1064px;
    height: 608px;
    background: var(--banner-black);
  }
  .banner__frame {
    position: absolute;
    left: 0;
    top: 0;
    width: 1064px;
    height: 608px;
  }
  .brand-name {
    position: absolute;
    left: 0;
    right: 0;
    top: 96px;
    text-align: center;
    font-weight: 900;
    font-size: 270px;
    line-height: 1;
    letter-spacing: -4px;
    color: var(--brand-orange);
  }
  .tagline {
    position: absolute;
    left: 0;
    right: 0;
    top: 420px;
    text-align: center;
    font-weight: 900;
    font-style: italic;
    font-size: 70px;
    line-height: 1;
    letter-spacing: 2px;
    color: var(--tagline-red);
  }
  .website {
    position: absolute;
    left: 0;
    right: 0;
    top: 520px;
    text-align: center;
    font-weight: 800;
    font-size: 60px;
    line-height: 1;
    color: var(--url-white);
  }
</style>
</head>
<body>
  <section class="banner">
    <svg class="banner__frame" viewBox="0 0 1064 608" aria-hidden="true">
      <path d="M217 562 H40 V33 H1034 V562 H850"
            fill="none" stroke="var(--frame-amber)" stroke-width="8"
            stroke-linecap="round" stroke-linejoin="round"/>
    </svg>
    <h1 class="brand-name">RVB</h1>
    <p class="tagline">TEMP LABOR</p>
    <p class="website">WWW.KTRVB.COM</p>
  </section>
</body>
</html>
```